Company Intro Banner for new company website

Harrowgate Components, Inc is a resistor manufacturer and a well known brand named HCI. We are creating a new customer facing web site that needs a well designed professional introduction in the form of a banner. There are several files attached to this project request. The Intro Banner Design Request.pdf file describes the project in full details.

Target Market(s)

Our primary audience are Electronic Design Engineers, Electronics Manufacturers (like Pindle, Corvanta, Brix, etc)

Industry/Entity Type

Electronics

Requirements
Must have
• Please refer to the narrative attached to this project.
Should not have
• The banner/tile should not over power our new web site design. It should augment the site and specifically tell folks that visit our new site they have come to HCI Harrowgate Components.

```html
<!DOCTYPE html>
<html lang="en">
<head>
<meta charset="utf-8">
<title>HCI Harrowgate Components – Resistive Product Solutions</title>
<link rel="stylesheet" href="https://fonts.googleapis.com/css2?family=Signika:wght@600&family=Roboto+Condensed:wght@700&display=swap">
<style>
  :root {
    --bg: #ffffff;
    --maroon: #5e0f16;
    --brand: #6b1a22;
    --band-dark: #4f1f4a;
    --band-mid: #7d3552;
    --band-light: #a4555b;
  }
  html, body {
    margin: 0;
    padding: 0;
    overflow: hidden;
    background: var(--bg);
  }
  .banner {
    position: relative;
    width: 1200px;
    height: 376px;
    overflow: hidden;
    background: var(--bg);
  }
  .banner__band {
    position: absolute;
    top: 0;
    left: 0;
    width: 1200px;
    height: 375px;
  }
  .brand {
    position: absolute;
    left: 70px;
    top: 108px;
    color: var(--brand);
    font-family: "Roboto Condensed", Arial, sans-serif;
    font-weight: 700;
  }
  .brand__mark {
    display: block;
    font-size: 84px;
    line-height: 1;
    letter-spacing: 2px;
  }
  .brand__name {
    display: block;
    margin-top: 6px;
    font-size: 13px;
    letter-spacing: 0.6px;
    text-transform: uppercase;
  }
  .headline {
    position: absolute;
    left: 294px;
    top: 222px;
    margin: 0;
    font-family: "Signika", Arial, sans-serif;
    font-weight: 600;
    font-size: 66px;
    line-height: 1;
    color: var(--maroon);
    text-shadow: 1px 2px 3px rgba(60, 10, 15, 0.35);
    white-space: nowrap;
  }
  .headline__reflection {
    position: absolute;
    left: 294px;
    top: 278px;
    margin: 0;
    font-family: "Signika", Arial, sans-serif;
    font-weight: 600;
    font-size: 66px;
    line-height: 1;
    color: var(--maroon);
    white-space: nowrap;
    transform: scaleY(-1);
    transform-origin: top;
    opacity: 0.25;
    -webkit-mask-image: linear-gradient(to top, rgba(0,0,0,1) 0%, rgba(0,0,0,0) 55%);
    mask-image: linear-gradient(to top, rgba(0,0,0,1) 0%, rgba(0,0,0,0) 55%);
    translate: 0 66px;
  }
</style>
</head>
<body>
  <div class="banner">
    <svg class="banner__band" viewBox="0 0 960 300" preserveAspectRatio="none"
         role="img" aria-label="Faceted triangle mosaic band in maroon and plum tones across the top edge">
      <defs>
        <linearGradient id="bandFill" x1="0" y1="0" x2="1" y2="1">
          <stop offset="0" stop-color="var(--band-dark)"/>
          <stop offset="0.55" stop-color="var(--band-mid)"/>
          <stop offset="1" stop-color="var(--band-light)"/>
        </linearGradient>
      </defs>
      <polygon fill="url(#bandFill)"
        points="0,0 960,0 960,70 845,82 845,55 760,62 700,80 728,130 670,140 650,95 620,95 590,120 555,130 500,140 470,145 440,145 400,128 330,130 325,88 270,95 270,130 210,118 212,95 150,80 100,65 40,57 0,40"/>
    </svg>

    <div class="brand">
      <span class="brand__mark">HCI</span>
      <span class="brand__name">Harrowgate Components, Inc.</span>
    </div>

    <h1 class="headline">Resistive Product Solutions</h1>
    <p class="headline__reflection" aria-hidden="true">Resistive Product Solutions</p>
  </div>
</body>
</html>
```